Fruits and Vegetables distribution company needs a new eye catching website

We need to get our website up to date. Our clients will look at our website to learn about our products and services. Our design needs to be simple yet impactful to make our brand memorable to our visitors. We need to have somewhere to tell our clients about our history, products and services, our team. We can throw in a few fun facts and figures and maybe some testimonials to impress. We have 4 theme colors that we want to incorporate into the design, you can get in touch for the HEX/RGB codes. Please remember that smooth operation of any animations and interactions is very important.

```html
<!DOCTYPE html>
<html lang="en">
<head>
<meta charset="utf-8">
<title>Zahra Fresh General Trading LLC</title>
<link rel="stylesheet" href="https://fonts.googleapis.com/css2?family=Roboto:wght@300;400;500;700&display=swap">
<style>
  :root {
    --green: #8dc63f;
    --orange: #f5b324;
    --red: #c8282d;
    --white: #ffffff;
    --ink: #333333;
  }
  * { margin: 0; padding: 0; box-sizing: border-box; }
  html, body { width: 1200px; height: 1000px; overflow: hidden; background: var(--white); }
  body { position: relative; font-family: 'Roboto', Arial, sans-serif; }

  .contact-bar { position: absolute; top: 0; left: 0; width: 1200px; height: 42px; }
  .contact-item { position: absolute; top: 0; height: 42px; display: flex; align-items: center; gap: 10px;
    color: var(--green); font-size: 16px; font-weight: 400; }
  .contact-phone { left: 730px; }
  .contact-email { left: 927px; gap: 16px; }

  .site-header { position: absolute; top: 42px; left: 0; width: 1200px; height: 112px; background: var(--green);
    border-bottom: 4px solid var(--orange); height: 116px; }
  .brand { position: absolute; left: 26px; top: 24px; color: var(--white); font-size: 58px; font-weight: 700;
    letter-spacing: 1px; line-height: 64px; }
  .main-nav { position: absolute; right: 24px; top: 37px; display: flex; height: 38px; }
  .main-nav a { display: flex; align-items: center; padding: 0 18px 0 23px; color: var(--white); text-decoration: none;
    font-size: 16px; font-weight: 500; border-right: 1.5px solid rgba(255,255,255,0.85); }
  .main-nav a:first-child { padding-left: 0; padding-right: 23px; }

  .hero { position: absolute; top: 158px; left: 0; width: 1200px; height: 449px; text-align: center; color: var(--white); }
  .hero-photo { position: absolute; inset: 0;
    background:
      radial-gradient(circle at 15% 70%, #b8a33a 0%, transparent 30%),
      radial-gradient(circle at 40% 75%, #b5281e 0%, transparent 25%),
      radial-gradient(circle at 80% 70%, #a8201a 0%, transparent 28%),
      radial-gradient(circle at 90% 20%, #c9a21a 0%, transparent 25%),
      radial-gradient(circle at 20% 20%, #7a8a2a 0%, transparent 30%),
      radial-gradient(circle at 60% 30%, #7e8f33 0%, transparent 25%),
      linear-gradient(135deg, #5a4a25, #3b2a1e 50%, #4a3020); }
  .hero-title { position: absolute; top: 140px; left: 0; width: 100%; font-size: 52px; font-weight: 700; line-height: 60px; }
  .hero-slogan { position: absolute; top: 247px; left: 0; width: 100%; font-size: 20px; font-weight: 400; }
  .quote-button { position: absolute; top: 314px; left: 459px; width: 282px; height: 56px; border-radius: 18px;
    background: var(--green); color: var(--white); font-size: 20px; font-weight: 500; line-height: 56px; text-decoration: none; }

  .products { position: absolute; top: 607px; left: 0; width: 1200px; text-align: center; }
  .section-title { margin-top: 42px; color: var(--green); font-size: 44px; font-weight: 700; line-height: 50px; }
  .section-intro { margin-top: 11px; color: var(--ink); font-size: 18px; font-weight: 300; line-height: 24px; }
  .section-rule { width: 176px; height: 3px; background: var(--orange); margin: 23px auto 0; }
  .product-card { position: absolute; top: 250px; width: 270px; height: 200px; }
  .card-carrots { left: 24px; background: linear-gradient(160deg, #3f6b2a 0%, #e06a1c 35%, #e87a22 100%); }
  .card-lemons { left: 318px; background: linear-gradient(160deg, #f0dc1e, #e8cf12 60%, #d9b90e); }
  .card-bananas { left: 612px; background: linear-gradient(160deg, #f2d23c, #e9c22a 60%, #c99a1a); }
  .card-tomatoes { left: 906px; background: linear-gradient(160deg, #d92a1e, #c81e16 60%, #a51812); }
</style>
</head>
<body>
  <div class="contact-bar">
    <div class="contact-item contact-phone">
      <svg width="22" height="24" viewBox="0 0 24 24" aria-hidden="true"><path fill="#c8282d" d="M6.6 10.8c1.4 2.8 3.8 5.1 6.6 6.6l2.2-2.2c.3-.3.7-.4 1-.2 1.1.4 2.3.6 3.6.6.6 0 1 .4 1 1V20c0 .6-.4 1-1 1C10.6 21 3 13.4 3 4c0-.6.4-1 1-1h3.5c.6 0 1 .4 1 1 0 1.3.2 2.5.6 3.6.1.3 0 .7-.2 1z"/></svg>
      <span>+971 (4) 555-0142</span>
    </div>
    <div class="contact-item contact-email">
      <svg width="40" height="26" viewBox="0 0 40 26" aria-hidden="true"><rect x="1" y="1" width="38" height="24" fill="#c8282d"/><path d="M2 2 L20 15 L38 2" fill="none" stroke="#fff" stroke-width="2"/></svg>
      <span>info@zahrafresh.com</span>
    </div>
  </div>

  <header class="site-header">
    <div class="brand">ZAHRA</div>
    <nav class="main-nav">
      <a href="#products">PRODUCTS AND SERVICES</a>
      <a href="#about">ABOUT US</a>
      <a href="#contacts">CONTACTS</a>
    </nav>
  </header>

  <section class="hero">
    <div class="hero-photo" role="img" aria-label="Photo of an assortment of fresh fruits and vegetables: grapes, tomatoes, peppers, bananas, lemons and broccoli"></div>
    <h1 class="hero-title">ZAHRA FRESH GENERAL TRADING LLC</h1>
    <p class="hero-slogan">SOMEHTING ABOUT THE COMPANY AND WHAT WE DO SLOGAN</p>
    <a class="quote-button" href="#quote">GET A QUOTE NOW</a>
  </section>

  <section class="products" id="products">
    <h2 class="section-title">PRODUCTS &amp; SERVICES</h2>
    <p class="section-intro">Lorem ipsum dolor sit amet, consectetur adipiscing elit. Nulla aliquet vestibulum orci, quis maximus tellus tincidunt nec.<br>Aliquam ullamcorper sapien at ex condimentum viverra</p>
    <div class="section-rule"></div>
    <div class="product-card card-carrots" role="img" aria-label="Photo of fresh carrots with green tops"></div>
    <div class="product-card card-lemons" role="img" aria-label="Photo of a pile of yellow lemons"></div>
    <div class="product-card card-bananas" role="img" aria-label="Photo of bunches of ripe bananas"></div>
    <div class="product-card card-tomatoes" role="img" aria-label="Photo of red vine tomatoes"></div>
  </section>
</body>
</html>
```